Book Cover for Self Help Book Teens

I need a standard a5 size book cover (front and back) for my new self help book for teens. The book is called
WHEN DAYS DRAG
ideas and tactics for teens in tough times
break ups, school problems, procrastination, fights, sexuality, alcohol, bitchiness, eating problems, can’t sleep, no motivation, not allowed to do stuff, being on the outer..and 34 other common situations that every day Australian teens face
Brenna Faldow
psychologist for teens
I would like a very sparse,very modern cover, no photos - maybe just cartoon-y graphic of smiley face upside down - ie frowny face. Few colours in order to make it look bold. lots of space on the cover.
I will provide back cover text soon
Updates
I just want to say that I really appreciate all of your efforts, the designs were excellent. As a thankyou, I'm happy to email you a link to the e-version of this book if you are interested. Just email me at brennafaldow@quillmarsh.example and I will send it through as soon as it is completed.
Target Market(s)
teens....but parents will also be buying book
Industry/Entity Type
School
Look and feel

```html
<!DOCTYPE html>
<html lang="en">
<head>
<meta charset="utf-8">
<title>When Days Drag — Cover</title>
<link rel="stylesheet" href="https://fonts.googleapis.com/css2?family=Amatic+SC:wght@400;700&family=Open+Sans:ital,wght@0,400;1,300;1,400&display=swap">
<style>
  :root {
    --bg: #272c28;
    --green-deep: #1f7a3e;
    --green-light: #86c540;
    --green-mid: #4fa53f;
    --green-muted: #7db87a;
    --text-light: #e6e9e4;
    --figure: #5aa83a;
  }
  * { margin: 0; padding: 0; box-sizing: border-box; }
  html, body { width: 847px; height: 1200px; overflow: hidden; background: var(--bg); }
  .cover {
    position: relative;
    width: 847px;
    height: 1200px;
    background: var(--bg);
    font-family: "Open Sans", sans-serif;
    color: var(--text-light);
  }
  .title {
    position: absolute;
    top: 40px;
    left: 0;
    width: 100%;
    text-align: center;
    font-family: "Amatic SC", cursive;
    font-weight: 700;
    font-size: 132px;
    line-height: 114px;
    letter-spacing: 8px;
  }
  .title span { display: block; }
  .title .word-1 { color: var(--green-deep); }
  .title .word-2 { color: var(--green-light); }
  .title .word-3 { color: var(--green-mid); }
  .subtitle {
    position: absolute;
    top: 428px;
    left: 0;
    width: 100%;
    text-align: center;
    font-style: italic;
    font-weight: 300;
    font-size: 28px;
    line-height: 36px;
  }
  .figures {
    position: absolute;
    top: 512px;
    left: 338px;
    width: 176px;
    height: 84px;
    background: var(--figure);
    opacity: 0.85;
    border-radius: 40px;
  }
  .author {
    position: absolute;
    top: 758px;
    left: 0;
    width: 100%;
    text-align: center;
    font-family: "Amatic SC", cursive;
    font-weight: 700;
    font-size: 58px;
    letter-spacing: 3px;
    color: var(--green-light);
  }
  .author-role {
    position: absolute;
    top: 818px;
    left: 0;
    width: 100%;
    text-align: center;
    font-style: italic;
    font-size: 27px;
  }
  .topics {
    position: absolute;
    top: 1090px;
    left: 14px;
    width: 820px;
    font-size: 21.5px;
    line-height: 24px;
  }
  .topics em { font-style: normal; color: var(--green-muted); }
</style>
</head>
<body>
<main class="cover">
  <h1 class="title">
    <span class="word-1">WHEN</span>
    <span class="word-2">DAYS</span>
    <span class="word-3">DRAG</span>
  </h1>
  <p class="subtitle">ideas and tactics for<br>teens in tough times</p>
  <div class="figures" role="img" aria-label="Three small green cartoon figures standing in a row"></div>
  <p class="author">Brenna Faldow</p>
  <p class="author-role">psychologist for teens</p>
  <p class="topics">
    break ups, <em>school problems</em>, procrastination, fights, <em>sexuality</em>, alcohol,<br>
    <em>bitchiness</em>, eating problems, <em>can't sleep</em>, no motivation, not allowed<br>
    to do stuff, being on the outer.. and <em>34 other</em> common <em>situations</em> that<br>
    every day <em>Australian teens</em> face
  </p>
</main>
</body>
</html>
```